Maelis Spacial\floral Decorator

Maelis is a spacial\floral decorator. She is passionate about Art, Life, Architecture, Painting, Music and movement. Her website will be used to showcase her spacial and floral design projects.
We are looking for a very unique website that stands apart from the crowd.
We believe that is achieved through simple high quality design Simple being very important.
The Home page should display primarily photos.
Your task is to provide an un-coded homepage template.
The page must be dynamic in its style and feel.

Maelis has suggest a grid pattern for the images, similar to this http://www.dorvanbloomhouse.co.uk. Overall We like the look and feel of this site.

We like the following color palettes, please base your design around one of them;
https://tintrova.example.com/#themes/search?term=5531704
https://tintrova.example.com/#themes/search?term=5536218
https://tintrova.example.com/#themes/search?term=5548126
https://tintrova.example.com/#themes/search?term=5540967
https://tintrova.example.com/#themes/search?term=5537419

Our target Market is High End Corporate Clients, located in Shanghai and Taipai. For these clients she utilise her floral and interior design skills to decorate a space. See Photos 2, 3 and 21 for examples.
She also targets High End personal clients for events such as weddings and gift combination i.e. flowers and something else.

Requirements
Must have
• Chinese/ English Language Selection
A selection of pictures that appear and disappear.
A menu system that includes:
Home – Portfolio – About Maelis – Blog – Contact Her
A very subtle menu system linking to chatnest, worklinq On, v+ and xunmo.
Nice to have
• We also like the use of an image for the background but this is not necessary.
Should not have
• Alot of Text, yes we now this isn't great for SEO but we will deal with that on other pages

```html
<!DOCTYPE html>
<html lang="en">
<head>
<meta charset="utf-8">
<title>Maelis — Portfolio</title>
<link rel="stylesheet" href="https://fonts.googleapis.com/css2?family=Questrial&family=Dancing+Script:wght@700&display=swap">
<style>
  :root {
    --plum: #3b3550;
    --plum-soft: #6e6685;
    --sage: #97c4ad;
    --sage-text: #9cc4ae;
    --ink: #3a3550;
    --grey-text: #8a8a8a;
    --page: #ffffff;
    --side: #d9d9d6;
  }
  * { margin: 0; padding: 0; box-sizing: border-box; }
  html, body { width: 1200px; height: 814px; overflow: hidden; }
  body {
    position: relative;
    font-family: "Questrial", "Century Gothic", sans-serif;
    color: var(--ink);
    background: linear-gradient(180deg, #cfd1cc 0%, #e6e7e3 30%, #dcdfd8 60%, #e9e9e6 100%);
  }
  .backdrop {
    position: absolute; inset: 0;
    background: linear-gradient(90deg, #c9ccc6 0%, #e4e6e1 8%, #e4e6e1 92%, #c9ccc6 100%);
  }
  .page {
    position: absolute; left: 100px; top: 0; width: 1000px; height: 814px;
    background: var(--page);
  }
  .hero-photo {
    position: absolute; left: 0; top: 70px; width: 1000px; height: 190px;
    background: linear-gradient(180deg, #c9c6c3 0%, #e3e2e0 45%, #ffffff 100%);
  }
  .topbar { position: absolute; left: 0; top: 0; width: 1000px; height: 62px; background: var(--page); }
  .topbar-band {
    position: absolute; left: 0; top: 61px; width: 1000px; height: 9px;
    background: linear-gradient(180deg, var(--plum) 0 4px, #ffffff 4px 5px, var(--sage) 5px 9px);
  }
  .nav-marker {
    position: absolute; left: 101px; top: 0;
    width: 0; height: 0;
    border-left: 9px solid transparent; border-right: 9px solid transparent;
    border-top: 8px solid var(--sage);
  }
  .main-nav { position: absolute; top: 22px; left: 0; font-size: 14px; }
  .main-nav a { position: absolute; white-space: nowrap; color: var(--ink); text-decoration: none; }
  .contact-line { position: absolute; left: 722px; top: 23px; display: flex; align-items: center; gap: 6px; font-size: 17px; color: var(--ink); }
  .divider { position: absolute; left: 864px; top: 18px; width: 2px; height: 28px; background: #dcdcdc; }
  .social-nav { position: absolute; left: 872px; top: 26px; display: flex; gap: 5px; font-size: 9.5px; }
  .social-nav a { color: var(--plum-soft); text-decoration: none; white-space: nowrap; }
  .brand-badge {
    position: absolute; left: 449px; top: -26px; width: 168px; height: 170px;
    border-radius: 50%; background: #fff;
    border-bottom: 4px solid var(--plum);
    box-shadow: 0 4px 0 -1px var(--sage);
    display: flex; align-items: flex-end; justify-content: center; padding-bottom: 52px;
  }
  .brand-name { font-size: 34px; color: var(--plum); letter-spacing: 1px; }
  .section-title { position: absolute; left: 47px; top: 162px; font-family: "Dancing Script", cursive; font-size: 32px; color: var(--plum); }
  .section-sub { position: absolute; left: 45px; top: 205px; font-size: 20px; color: var(--sage-text); }
  .tile {
    position: absolute; border: 3px solid var(--plum-soft);
  }
  .tile-overlay {
    display: flex; align-items: center; justify-content: center;
    background: var(--sage); color: #fff; font-size: 12px; font-weight: bold;
  }
  .pager { position: absolute; top: 687px; left: 468px; display: flex; gap: 8px; }
  .pager span { width: 12px; height: 12px; border-radius: 50%; background: #444; box-shadow: 0 0 0 1px #aaa inset; }
  .footer {
    position: absolute; left: 0; top: 745px; width: 1000px; height: 69px;
    background: linear-gradient(180deg, #f1f1f1 0%, #fafafa 40%, #ececec 100%);
    border-top: 1px dashed #dedede;
    text-align: center; font-size: 12px; color: var(--grey-text);
  }
  .footer-nav { margin-top: 16px; }
  .footer-nav a { color: var(--grey-text); text-decoration: none; }
  .footer-nav .sep { margin: 0 7px; }
  .copyright { margin-top: 7px; }
</style>
</head>
<body>
<div class="backdrop" role="img" aria-label="Faded photograph of a decorated event space with white flowers"></div>

<div class="page">
  <div class="hero-photo" role="img" aria-label="Faded photograph of a banquet table set with glasses and floral centrepieces"></div>

  <header class="topbar">
    <span class="nav-marker"></span>
    <nav class="main-nav">
      <a href="#" style="left:21px">Home</a>
      <a href="#" style="left:84px">Portfolio</a>
      <a href="#" style="left:160px">About Maelis</a>
      <a href="#" style="left:260px">Blog</a>
      <a href="#" style="left:313px">Contact Her</a>
    </nav>
    <div class="contact-line">
      <svg width="13" height="16" viewBox="0 0 13 16" aria-hidden="true"><path d="M3 1 L5.5 1 L6.5 5 L4.6 6.3 C5.3 8.5 6.5 10.2 8.2 11.4 L9.8 9.9 L12.5 11.8 L11.6 14.6 C6 14.5 1.5 8 1.6 2.2 Z" fill="#3b3550"/></svg>
      <span>0555 2846 317</span>
    </div>
  </header>
  <div class="topbar-band"></div>
  <span class="divider"></span>
  <nav class="social-nav" aria-label="Social">
    <a href="#">chatnest</a><a href="#">v+</a><a href="#">worklinq On</a><a href="#">xunmo</a>
  </nav>

  <div class="brand-badge"><span class="brand-name">Maelis</span></div>

  <h1 class="section-title">Portfolio</h1>
  <p class="section-sub">flowers decorations</p>

  <section class="portfolio-grid">
    <div class="tile" style="left:45px;top:251px;width:172px;height:122px;background:linear-gradient(135deg,#8a1f35,#c9c2c0 55%,#6b3a3f)" role="img" aria-label="Red roses beside a white vase"></div>
    <div class="tile" style="left:230px;top:251px;width:171px;height:122px;background:linear-gradient(135deg,#e8e6e0,#7a9a3a 55%,#4a3d30)" role="img" aria-label="Green arrangement with blue agapanthus"></div>
    <div class="tile" style="left:413px;top:251px;width:172px;height:122px;background:linear-gradient(135deg,#b0101e,#7d0a16 60%,#3f5a2c)" role="img" aria-label="Bouquet of red roses"></div>
    <div class="tile" style="left:600px;top:251px;width:172px;height:122px;background:linear-gradient(135deg,#3a3232,#d98aa8 50%,#6a6460)" role="img" aria-label="Pink lilies on a market stall"></div>
    <div class="tile" style="left:789px;top:251px;width:172px;height:122px;background:linear-gradient(135deg,#d8d0e0,#4f8a3a 50%,#b52020)" role="img" aria-label="Red and green flower arrangement"></div>

    <div class="tile" style="left:45px;top:379px;width:172px;height:122px;background:linear-gradient(135deg,#b07a20,#5c8a3a 50%,#d8c0d8)" role="img" aria-label="Lilac lisianthus with a golden statue"></div>
    <div class="tile tile-overlay" style="left:230px;top:379px;width:171px;height:122px"><span>view large</span></div>
    <div class="tile" style="left:413px;top:379px;width:172px;height:122px;background:linear-gradient(135deg,#2e4fb0,#c8d070 45%,#2f5a2a)" role="img" aria-label="Yellow orchids on blue glass"></div>
    <div class="tile" style="left:600px;top:379px;width:172px;height:122px;background:linear-gradient(135deg,#3a3232,#d98aa8 50%,#6a6460)" role="img" aria-label="Pink lilies on a market stall"></div>
    <div class="tile" style="left:789px;top:379px;width:172px;height:122px;background:linear-gradient(135deg,#2f5a2a,#d8e8c0 55%,#4a6a30)" role="img" aria-label="White-green lisianthus blooms"></div>

    <div class="tile" style="left:45px;top:512px;width:172px;height:122px;background:linear-gradient(135deg,#8a1f35,#c9c2c0 55%,#6b3a3f)" role="img" aria-label="Red roses beside a white vase"></div>
    <div class="tile" style="left:230px;top:512px;width:171px;height:122px;background:linear-gradient(135deg,#e8e6e0,#7a9a3a 55%,#4a3d30)" role="img" aria-label="Green arrangement with blue agapanthus"></div>
    <div class="tile" style="left:413px;top:512px;width:172px;height:122px;background:linear-gradient(135deg,#b0101e,#7d0a16 60%,#3f5a2c)" role="img" aria-label="Bouquet of red roses"></div>
    <div class="tile" style="left:600px;top:512px;width:172px;height:122px;background:linear-gradient(135deg,#3a3232,#d98aa8 50%,#6a6460)" role="img" aria-label="Pink lilies on a market stall"></div>
    <div class="tile" style="left:789px;top:512px;width:172px;height:122px;background:linear-gradient(135deg,#d8d0e0,#4f8a3a 50%,#b52020)" role="img" aria-label="Red and green flower arrangement"></div>
  </section>

  <div class="pager" aria-label="Pages"><span></span><span></span><span></span><span></span></div>

  <footer class="footer">
    <nav class="footer-nav">
      <a href="#">Home</a><span class="sep">|</span><a href="#">Portfolio</a><span class="sep">|</span><a href="#">About Maelis</a><span class="sep">|</span><a href="#">Blog</a><span class="sep">|</span><a href="#">Contact Her</a>
    </nav>
    <p class="copyright">Copyrights All Rights Reserved</p>
  </footer>
</div>
</body>
</html>
```